Ridgecrest Balusters Website Redesign

I want a fresh new design for my website. Original website
www.ridgecrestbalusters.example. Will need to add additional photos for winning designer. Please use the basic layout for new design. Looking to get a more modern, functional site to attract new customer and ne bale to highlight past projects. Need it to be easy to navigate and get in touch with me for inquiries.

Target Market(s)

Builders and home owners in WA state

Industry/Entity Type

Building, Construction, Deck building

Coding

Coded - Design and coding required

Number of Pages Required

5+ page

Font styles to use
Sans Serif

Colors
0054AA
0677BA
7BADD7
CADEEF
E8F1F8
0094D4
00A9DD
6FCCEA
C7EBF8
E9F6FB
00AB8E
00BBA5
67D7C9
C6EFE9
E9F9F6
59FF00
82FF00
B8FF75
E3FFCB
F4FFEA

Requirements
Must have
• Will need to add more photos of completed projects
Nice to have
• Fresh take on old website, something modern
Should not have
• Nothing comes to mind

```html
<!DOCTYPE html>
<html lang="en">
<head>
<meta charset="utf-8">
<title>Ridgecrest Balusters</title>
<link rel="stylesheet" href="https://fonts.googleapis.com/css2?family=EB+Garamond:wght@400;500;600;700&display=swap">
<style>
:root{
  --green:#00AB8E;
  --green-deep:#12996f;
  --mint:#e1ece6;
  --ink:#2b2b2b;
  --text:#555;
  --white:#fff;
  --footer:#2a2a2a;
}
*{box-sizing:border-box;margin:0;padding:0}
html,body{width:1200px;height:4580px;overflow:hidden}
body{position:relative;font-family:"EB Garamond",Georgia,serif;color:var(--text);background:var(--white)}
.abs{position:absolute}
.btn{position:absolute;background:var(--green);color:var(--white);font-weight:600;font-size:15px;display:flex;align-items:center;justify-content:center;border-radius:3px}
.section-title{position:absolute;left:0;width:1200px;text-align:center;color:var(--green-deep);font-weight:500;font-size:37px;line-height:1}
.photo{position:absolute}

/* header */
.site-header{position:absolute;left:0;top:0;width:1200px;height:74px;background:var(--white);z-index:2}
.brand-box{position:absolute;left:0;top:0;width:214px;height:165px;background:var(--white);border-bottom-right-radius:34px;z-index:3;display:flex;align-items:center;padding-left:30px}
.brand-name{font-size:30px;line-height:1.05;font-weight:600;color:var(--green-deep)}
.main-nav{position:absolute;left:447px;top:26px;display:flex;gap:0}
.main-nav a{font-size:15px;color:#222;text-decoration:none;font-weight:500;margin-right:30px}
.main-nav a.active{color:var(--green)}
.nav-contact{left:999px;top:20px;width:139px;height:34px}

/* hero */
.hero{position:absolute;left:0;top:73px;width:1200px;height:549px}
.hero-photo{inset:0;background:linear-gradient(100deg,#5d6350 0%,#4a4a45 30%,#3d3d3d 55%,#2e2e2c 80%,#4a4a42 100%)}
.hero-title{position:absolute;left:0;top:196px;width:1200px;text-align:center;color:var(--white);font-size:43px;font-weight:500}
.hero-sub{position:absolute;left:270px;top:262px;width:660px;text-align:center;color:#eee;font-size:13px;line-height:1.4}
.hero-btn{left:530px;top:318px;width:139px;height:32px}
.hero-arrow{position:absolute;top:249px;width:50px;height:50px;border-radius:50%;background:var(--white);display:flex;align-items:center;justify-content:center}

/* about */
.about-photo{left:62px;top:684px;width:516px;height:388px;background:linear-gradient(180deg,#b9c5d2 0%,#8d97a0 45%,#4e5155 70%,#7c7c78 100%)}
.exp-badge{position:absolute;left:432px;top:1004px;width:146px;height:68px;background:var(--white);border-top-left-radius:16px;display:flex;align-items:center;gap:10px;padding-left:10px}
.exp-badge .dot{width:40px;height:40px;border-radius:50%;background:var(--green);color:var(--white);font-size:15px;font-weight:600;display:flex;align-items:center;justify-content:center}
.exp-badge .label{font-size:17px;line-height:1.1;color:#222;font-weight:500}
.about-title{position:absolute;left:633px;top:742px;font-size:38px;color:var(--green-deep);font-weight:500}
.about-text{position:absolute;left:633px;top:800px;width:508px;font-size:12.5px;line-height:1.45;color:#666}
.about-text p{margin-bottom:8px}
.about-btn{left:633px;top:978px;width:139px;height:32px}

/* products */
.products{position:absolute;left:0;top:1134px;width:1200px;height:559px;background:var(--mint)}
.card{position:absolute;background:var(--white);box-shadow:0 2px 6px rgba(0,0,0,.08)}
.card .label{position:absolute;left:0;bottom:0;width:100%;display:flex;align-items:center;justify-content:center;font-size:14px;font-weight:600;color:#222;text-transform:uppercase}
.card.active .label{background:var(--green);color:var(--white)}
.dots{position:absolute;display:flex;gap:6px}
.dots span{width:27px;height:5px;background:var(--white);border-radius:2px}
.dots span.on{background:var(--green)}
.dots.grey span{background:#aaa}
.dots.grey span.on{background:var(--green)}

/* why */
.why-card{position:absolute;width:519px;border-radius:4px;overflow:hidden;color:var(--white);text-align:center}
.why-card .bg{position:absolute;inset:0}
.why-card .shade{position:absolute;inset:0;background:rgba(0,0,0,.5)}
.why-card .icon{position:absolute;left:223px;top:24px;width:72px;height:72px;border-radius:50%;background:var(--white);display:flex;align-items:center;justify-content:center}
.why-card h3{position:absolute;left:0;top:106px;width:100%;font-size:15px;font-weight:600;text-transform:uppercase}
.why-card p{position:absolute;left:20px;top:136px;width:479px;font-size:12.5px;line-height:1.45;color:#e6e6e6}

/* projects */
.projects{position:absolute;left:0;top:2361px;width:1200px;height:581px;background:var(--mint)}
.project{position:absolute;top:123px;width:519px;height:348px;background:var(--white)}
.project .thumb{position:absolute;width:227px;height:125px}
.project .caption{position:absolute;left:0;top:308px;width:100%;text-align:center;font-size:14px;font-weight:600;color:#222;text-transform:uppercase}

/* accessories */
.acc{position:absolute;top:3090px;width:317px;height:364px;background:var(--white);border:1px solid #ddd;box-shadow:0 2px 6px rgba(0,0,0,.08)}
.acc .label{position:absolute;left:0;top:308px;width:100%;height:56px;display:flex;align-items:center;justify-content:center;font-size:14px;font-weight:600;color:#222;text-transform:uppercase}
.acc.active{border-color:var(--green)}
.acc.active .label{color:var(--green)}

/* quote */
.quote{position:absolute;left:0;top:3547px;width:1200px;height:643px}
.quote-bg{inset:0;background:linear-gradient(180deg,#2c3130 0%,#273235 50%,#1f2a30 100%)}
.quote-shade{position:absolute;inset:0;background:rgba(0,0,0,.35)}
.quote-title{position:absolute;left:0;top:78px;width:1200px;text-align:center;color:var(--white);font-size:37px;font-weight:500;letter-spacing:1px}
.field{position:absolute;background:var(--white);border-radius:3px;font-size:13px;color:#888;padding:18px 20px}
.submit{left:192px;top:524px;width:816px;height:32px}

/* footer */
.site-footer{position:absolute;left:0;top:4190px;width:1200px;height:390px;background:var(--footer);color:#ddd}
.footer-brand{position:absolute;left:62px;top:52px;display:flex;align-items:center;gap:12px}
.footer-brand .sq{width:22px;height:22px;background:var(--white)}
.footer-brand .name{font-size:34px;line-height:1.05;color:var(--white);font-weight:600}
.footer-about{position:absolute;left:62px;top:242px;width:320px;font-size:12.5px;line-height:1.4;color:#ccc}
.footer-col{position:absolute;top:30px}
.footer-col h4{font-size:20px;color:var(--green);font-weight:500;margin-bottom:18px}
.footer-col li{list-style:none;font-size:13.5px;color:#ddd;height:37px}
.contact-item{display:flex;gap:10px;font-size:13.5px;line-height:1.25;color:#ddd;margin-bottom:16px}
.contact-item .ic{flex:none;width:22px;height:22px;border-radius:50%;background:var(--white);display:flex;align-items:center;justify-content:center}
.footer-rule{position:absolute;left:62px;top:326px;width:1076px;height:1px;background:#555}
.footer-copy{position:absolute;left:62px;top:354px;font-size:13px;color:#ccc}
.footer-legal{position:absolute;right:62px;top:354px;font-size:13px;color:#ccc}
</style>
</head>
<body>

<header class="site-header">
  <nav class="main-nav">
    <a class="active">Home</a><a>About Us</a><a>Products</a><a>Railing Project</a><a>Remodel Projects</a>
  </nav>
  <a class="btn nav-contact">Contact</a>
</header>
<div class="brand-box"><span class="brand-name">Ridgecrest<br>Balusters</span></div>

<section class="hero">
  <div class="photo hero-photo" role="img" aria-label="Modern home exterior with black metal stair railing"></div>
  <h1 class="hero-title">Enhancing Homes, One Railing at a Time</h1>
  <p class="hero-sub">weather in mind rain, snow, and everything in between. We use durable materials that are resistant to corrosion, moisture, and the elements, ensuring your railings stand the test of time.</p>
  <a class="btn hero-btn">Contact</a>
  <span class="hero-arrow" style="left:64px"><svg width="22" height="14" viewBox="0 0 22 14"><path d="M21 7H2M8 1L2 7l6 6" fill="none" stroke="#00AB8E" stroke-width="2"/></svg></span>
  <span class="hero-arrow" style="left:1086px"><svg width="22" height="14" viewBox="0 0 22 14"><path d="M1 7h19M14 1l6 6-6 6" fill="none" stroke="#00AB8E" stroke-width="2"/></svg></span>
</section>

<section class="about">
  <div class="photo about-photo" role="img" aria-label="Two-storey house with glass deck railing and exterior staircase"></div>
  <div class="exp-badge"><span class="dot">15+</span><span class="label">Years Of<br>Experience</span></div>
  <h2 class="about-title">About Us</h2>
  <div class="about-text">
    <p>At Ridgecrest Balusters, we believe that every outdoor space deserves the perfect blend of style, safety, and durability. Serving homeowners, builders, and commercial developers across the Washington State, we specialize in crafting custom railing systems designed to withstand the region's unique climate while enhancing the beauty of your outdoor living spaces.</p>
    <p>With a focus on premium materials, expert craftsmanship, and exceptional customer service, Ridgecrest Balusters is proud to be the trusted partner for both residential and commercial railing projects.</p>
  </div>
  <a class="btn about-btn">Read More</a>
</section>

<section class="products">
  <h2 class="section-title" style="top:62px">Modern Stair Railings with a Sleek Finish</h2>
  <div class="card active" style="left:62px;top:130px;width:246px;height:341px">
    <div class="photo" style="left:0;top:0;width:246px;height:277px;background:linear-gradient(160deg,#c9a49a,#6f6f78 60%,#555)" role="img" aria-label="Aluminum railing on a patio with a bench"></div>
    <div class="label" style="height:64px">Aluminum Railings</div>
  </div>
  <div class="card" style="left:339px;top:130px;width:246px;height:341px">
    <div class="photo" style="left:0;top:0;width:246px;height:277px;background:linear-gradient(180deg,#9fb9d4,#6f8a6a 50%,#8e8e8c)" role="img" aria-label="Glass railing on a deck overlooking a valley"></div>
    <div class="label" style="height:64px">Glass Railing</div>
  </div>
  <div class="card" style="left:616px;top:130px;width:246px;height:341px">
    <div class="photo" style="left:0;top:0;width:246px;height:277px;background:linear-gradient(160deg,#4d5c48,#6d7277 50%,#9a9a98)" role="img" aria-label="Cable railing along exterior stairs"></div>
    <div class="label" style="height:64px">Cable Railing</div>
  </div>
  <div class="card" style="left:893px;top:130px;width:246px;height:341px">
    <div class="photo" style="left:0;top:0;width:246px;height:277px;background:linear-gradient(160deg,#f1f1f1,#9a9a9a 60%,#3a3a3a)" role="img" aria-label="Ornate custom spiral staircase railing"></div>
    <div class="label" style="height:64px">Custom Railing</div>
  </div>
  <div class="dots" style="left:553px;top:496px"><span class="on"></span><span></span><span></span></div>
</section>

<section class="why">
  <h2 class="section-title" style="top:1758px">Why Choose Ridgecrest Balusters ?</h2>
  <div class="why-card" style="left:62px;top:1828px;height:215px">
    <div class="bg" style="background:linear-gradient(135deg,#5a4a3c,#3a332c)" role="img" aria-label="Brick wall with dark metal railing"></div><div class="shade"></div>
    <span class="icon"><svg width="36" height="30" viewBox="0 0 36 30" fill="none" stroke="#00AB8E" stroke-width="2"><rect x="2" y="2" width="32" height="26"/><path d="M2 11h32M2 20h32M12 2v9M24 11v9M12 20v8"/></svg></span>
    <h3>Locally Crafted, Regionally Resilient</h3>
    <p>Our railings are designed with the Pacific Northwest's weather in mind rain, snow, and everything in between. We use durable materials that are resistant to corrosion, moisture, and the elements, ensuring your railings stand the test of time.</p>
  </div>
  <div class="why-card" style="left:619px;top:1828px;height:215px">
    <div class="bg" style="background:linear-gradient(135deg,#6b6b6b,#3e3e3e)" role="img" aria-label="Black railing on a deck in snow"></div><div class="shade"></div>
    <span class="icon"><svg width="34" height="34" viewBox="0 0 34 34" fill="none" stroke="#00AB8E" stroke-width="2"><circle cx="17" cy="17" r="6"/><circle cx="17" cy="17" r="13" stroke-dasharray="5 3"/></svg></span>
    <h3>Custom Solutions for Every Need</h3>
    <p>We work closely with you to design and fabricate custom railing systems that perfectly suit your space, style, and functional requirements. From intricate designs to minimalistic finishes, we tailor every project to your vision.</p>
  </div>
  <div class="why-card" style="left:62px;top:2082px;height:217px">
    <div class="bg" style="background:linear-gradient(135deg,#4a4f55,#2f3236)" role="img" aria-label="Consultation meeting in a bright office"></div><div class="shade"></div>
    <span class="icon"><svg width="34" height="34" viewBox="0 0 34 34" fill="none" stroke="#00AB8E" stroke-width="2"><circle cx="17" cy="17" r="14"/><path d="M10 17l5 5 9-10"/></svg></span>
    <h3>Full-Service Partner</h3>
    <p>From the initial consultation and design process to installation and ongoing maintenance, we are with you every step of the way to ensure your project exceeds expectations.</p>
  </div>
  <div class="why-card" style="left:619px;top:2082px;height:217px">
    <div class="bg" style="background:linear-gradient(135deg,#6a6a66,#2e2c2a)" role="img" aria-label="Installed railing on a finished deck"></div><div class="shade"></div>
    <span class="icon"><svg width="34" height="34" viewBox="0 0 34 34" fill="none" stroke="#00AB8E" stroke-width="2"><circle cx="17" cy="12" r="6"/><path d="M6 31c1-7 5-11 11-11s10 4 11 11"/></svg></span>
    <h3>Expert Installation &amp; Craftsmanship</h3>
    <p>Our skilled craftsmen take pride in delivering exceptional workmanship, while our professional installers ensure every railing is securely mounted and aligned to meet local safety codes.</p>
  </div>
</section>

<section class="projects">
  <h2 class="section-title" style="top:53px">Real-Life Railings Inspiration from Our Projects</h2>
  <div class="project" style="left:62px">
    <div class="photo thumb" style="left:22px;top:19px;background:linear-gradient(180deg,#6e5640,#c9ccd0)" role="img" aria-label="Covered deck railing with snowy view"></div>
    <div class="photo thumb" style="left:269px;top:19px;background:linear-gradient(180deg,#d9cfc3,#4a3a2c)" role="img" aria-label="Interior balcony railing"></div>
    <div class="photo thumb" style="left:22px;top:165px;background:linear-gradient(180deg,#e6e6e4,#6a6a66)" role="img" aria-label="Interior stair railing"></div>
    <div class="photo thumb" style="left:269px;top:165px;background:linear-gradient(180deg,#6e4a2c,#cfd2d4)" role="img" aria-label="Timber porch railing in snow"></div>
    <div class="caption">Timberline Custom Home; Cle Elum, WA</div>
  </div>
  <div class="project" style="left:619px">
    <div class="photo thumb" style="left:22px;top:19px;background:linear-gradient(180deg,#c8d3de,#6e6458)" role="img" aria-label="Apartment patio railing"></div>
    <div class="photo thumb" style="left:269px;top:19px;background:linear-gradient(180deg,#b9c3cc,#5e5e5a)" role="img" aria-label="Black picket railing on deck"></div>
    <div class="photo thumb" style="left:22px;top:165px;background:linear-gradient(180deg,#b5a68e,#e8e8e6)" role="img" aria-label="Balcony railings on apartment building"></div>
    <div class="photo thumb" style="left:269px;top:165px;background:linear-gradient(180deg,#c8d2dc,#9a9284)" role="img" aria-label="Stacked balconies with railings"></div>
    <div class="caption">New Senior Apartments; Omak, WA</div>
  </div>
  <a class="btn" style="left:505px;top:498px;width:188px;height:32px">View All</a>
</section>

<section class="accessories">
  <h2 class="section-title" style="top:3008px">Railing Accessories: The Perfect Finishing Touch</h2>
  <div class="acc active" style="left:62px">
    <div class="photo" style="left:0;top:0;width:315px;height:308px;background:linear-gradient(180deg,#1e1e1e,#3a3a3a 60%,#111)" role="img" aria-label="White base plate covers on railing posts"></div>
    <div class="label">Base Plate Covers</div>
  </div>
  <div class="acc" style="left:441px">
    <div class="photo" style="left:0;top:0;width:315px;height:308px;background:linear-gradient(180deg,#aec4d8,#6f7a60 45%,#8a8a86)" role="img" aria-label="Railing gate on deck overlooking town"></div>
    <div class="label">Gate Kits</div>
  </div>
  <div class="acc" style="left:820px">
    <div class="photo" style="left:0;top:0;width:315px;height:308px;background:linear-gradient(180deg,#c9d4dc,#8c8a72 50%,#b79a78)" role="img" aria-label="Fascia-mounted glass railing on elevated deck"></div>
    <div class="label">Fascia Mount</div>
  </div>
  <div class="dots grey" style="left:553px;top:3479px"><span class="on"></span><span></span><span></span></div>
</section>

<section class="quote">
  <div class="photo quote-bg" role="img" aria-label="Dark deck with black railing at dusk"></div>
  <div class="quote-shade"></div>
  <h2 class="quote-title">REQUEST A QUOTE</h2>
  <div class="field" style="left:192px;top:153px;width:395px;height:57px">Name</div>
  <div class="field" style="left:613px;top:153px;width:395px;height:57px">Last Name</div>
  <div class="field" style="left:192px;top:229px;width:816px;height:57px">E-Mail</div>
  <div class="field" style="left:192px;top:304px;width:816px;height:57px">Subject</div>
  <div class="field" style="left:192px;top:379px;width:816px;height:124px">How Can We Help You ?</div>
  <a class="btn submit">Submit</a>
</section>

<footer class="site-footer">
  <div class="footer-brand"><span class="sq"></span><span class="name">Ridgecrest<br>Balusters</span></div>
  <p class="footer-about">At Ridgecrest Balusters, we believe that every outdoor space deserves the perfect blend of style, safety, and durability.</p>
  <div class="footer-col" style="left:482px">
    <h4>Quick Links</h4>
    <ul><li>Home</li><li>About Us</li><li>Products</li><li>Railing Project</li><li>Remodel Projects</li></ul>
  </div>
  <div class="footer-col" style="left:708px">
    <h4>Our Products</h4>
    <ul><li>Glass Railing</li><li>Cable Railing</li><li>Custom Railing</li><li>Horizontal Railing</li><li>Aluminum Railing</li></ul>
  </div>
  <div class="footer-col" style="left:944px">
    <h4>Contact Info</h4>
    <div class="contact-item"><span class="ic"><svg width="12" height="12" viewBox="0 0 12 12"><path d="M2 1l2 0 1 3-1.5 1a6 6 0 003 3L8 7l3 1v2a1 1 0 01-1 1A9 9 0 011 2a1 1 0 011-1z" fill="#00AB8E"/></svg></span><span>(509) 555-0148</span></div>
    <div class="contact-item"><span class="ic"><svg width="12" height="12" viewBox="0 0 12 12"><path d="M6 1a3.5 3.5 0 013.5 3.5C9.5 7 6 11 6 11S2.5 7 2.5 4.5A3.5 3.5 0 016 1z" fill="#00AB8E"/><circle cx="6" cy="4.5" r="1.2" fill="#fff"/></svg></span><span>4120 Orchard Ridge Rd<br>Yakima, WA 98901</span></div>
    <div class="contact-item"><span class="ic"><svg width="12" height="10" viewBox="0 0 12 10"><rect x="1" y="1" width="10" height="8" fill="none" stroke="#00AB8E" stroke-width="1.5"/><path d="M1 1l5 4 5-4" fill="none" stroke="#00AB8E" stroke-width="1.5"/></svg></span><span>info@ridgecrestbalusters.example</span></div>
  </div>
  <div class="footer-rule"></div>
  <p class="footer-copy">© 2024 All Rights Reserved</p>
  <p class="footer-legal">Privacy Policy &nbsp;|&nbsp; Terms &amp; Condition</p>
</footer>

</body>
</html>
```